table invoices in a modern format! (make it fun to look at!!)

Our has invoices that are shown to our clients. This is currently done in a normal table view, but its boring to look at and is not modern.
We would like to have a modern look and feel
it should ABSOLUTLY not be in table form.
Cards, graphs, pictures, whatever... should be fun and almost interactive.

the table file is how it current looks like.
the other two files were "ideas" to have a better representation
IT DOES NOT NEED TO LOOK LIKE THAT if you have a better idea please go for it.

secondary objective, the graphs/cards/whatever you design should be interactive, meaning I can "click on it" to pay a bill, or see more info.

Let me know if there are more questions!

```html
<!DOCTYPE html>
<html lang="en">
<head>
<meta charset="utf-8">
<title>Invoice 2019</title>
<link href="https://fonts.googleapis.com/css2?family=Fredoka:wght@500;600;700&family=Montserrat:wght@600;700;800&display=swap" rel="stylesheet">
<style>
  :root {
    --bg: #333f47;
    --header-bg: #2a3238;
    --panel: #13455a;
    --ink: #13455a;
    --cream: #f7f1e3;
    --coral: #ff7553;
    --orange: #ff7a1f;
    --cyan-bright: #1ceeff;
    --cyan-soft: #7ae0e6;
    --green: #54c596;
    --yellow: #f0d06e;
    --lime: #c8d665;
    --year-box: #e3f1f3;
  }
  * { box-sizing: border-box; margin: 0; padding: 0; }
  html, body { width: 1200px; height: 750px; overflow: hidden; }
  body {
    position: relative;
    background: var(--bg);
    font-family: "Montserrat", sans-serif;
    color: var(--ink);
  }
  .abs { position: absolute; }

  .title-block { left: 0; top: 0; width: 440px; height: 107px; background: var(--header-bg); }
  .title {
    left: 27px; top: 14px; font-family: "Montserrat", sans-serif; font-weight: 800;
    font-size: 64px; line-height: 1; color: var(--year-box); letter-spacing: -1px;
  }
  .year-box {
    left: 306px; top: 28px; width: 98px; height: 47px; background: var(--year-box);
    display: flex; align-items: center; justify-content: center;
    font-family: "Fredoka", sans-serif; font-weight: 600; font-size: 31px;
    color: var(--ink); text-decoration: underline; text-decoration-thickness: 2px; text-underline-offset: 3px;
  }
  .year-stepper { left: 412px; top: 31px; }

  .overview-btn {
    left: 893px; top: 18px; width: 237px; height: 75px; background: var(--coral);
    box-shadow: 0 0 18px rgba(255,117,83,.45);
    display: flex; align-items: center; justify-content: center;
    font-family: "Fredoka", sans-serif; font-weight: 600; font-size: 30px; color: var(--cream);
  }

  .panel { left: 61px; top: 154px; width: 1078px; height: 413px; background: var(--panel); box-shadow: 0 6px 20px rgba(0,0,0,.25); }

  .donut { left: 99px; top: 181px; }
  .invoice-id {
    left: 135px; top: 304px; width: 200px; text-align: center;
    font-family: "Fredoka", sans-serif; font-weight: 600; font-size: 23px; color: var(--cream);
  }

  .style-toggle { left: 151px; top: 478px; width: 168px; height: 47px; background: var(--coral); }
  .toggle-pie {
    left: 6px; top: 6px; width: 70px; height: 35px; background: var(--panel);
    display: flex; align-items: center; justify-content: center;
    font-weight: 800; font-size: 27px; color: var(--coral);
  }
  .toggle-bar {
    left: 84px; top: 6px; width: 78px; height: 35px; display: flex; align-items: center; justify-content: center;
    font-weight: 800; font-size: 27px; color: var(--cream);
  }
  .toggle-hint { left: 135px; top: 530px; width: 200px; text-align: center; font-size: 10px; font-weight: 700; color: var(--cream); }

  .info-card {
    display: flex; flex-direction: column; align-items: center; justify-content: center;
    text-align: center;
  }
  .label { font-size: 11px; font-weight: 700; text-decoration: underline; text-underline-offset: 2px; }
  .info-card .value { font-family: "Fredoka", sans-serif; font-weight: 600; font-size: 26px; line-height: 1.05; }

  .month { left: 427px; top: 214px; width: 168px; height: 51px; background: var(--cyan-bright); }
  .status { left: 604px; top: 214px; width: 168px; height: 51px; background: var(--lime); }
  .mode { left: 782px; top: 214px; width: 168px; height: 51px; background: var(--cyan-bright); }

  .pdf-btn {
    left: 1034px; top: 214px; width: 84px; height: 51px; background: var(--orange);
    display: flex; align-items: center; justify-content: center;
    font-family: "Fredoka", sans-serif; font-weight: 700; font-size: 31px; color: var(--cream);
  }
  .pdf-edit { right: 5px; bottom: 3px; }

  .rule { left: 421px; width: 709px; height: 3px; background: var(--cream); }
  .rule-top { top: 277px; }
  .rule-bottom { top: 444px; }

  .amount-card { width: 145px; height: 100px; top: 318px; }
  .amount-card .label { position: absolute; top: 10px; left: 0; width: 100%; text-align: center; font-size: 12px; }
  .amount-card .value {
    position: absolute; top: 36px; left: 0; width: 100%; text-align: center;
    font-family: "Fredoka", sans-serif; font-weight: 700; font-size: 46px; letter-spacing: 1px;
  }
  .amount-bar { width: 145px; height: 6px; top: 423px; border-radius: 3px; }
  .received { left: 427px; background: var(--cyan-soft); }
  .extra { left: 600px; background: var(--green); }
  .contract { left: 773px; background: var(--yellow); }

  .mini-card { left: 950px; width: 168px; height: 51px; background: var(--lime); }
  .mini-card .value { font-size: 24px; }
  .open-balance { top: 318px; }
  .contract-days { top: 377px; }

  .side-arrow { top: 313px; width: 68px; height: 68px; border-radius: 50%; background: var(--year-box); }
  .side-prev { left: -34px; }
  .side-next { left: 1166px; }

  .summary-pill {
    top: 606px; width: 155px; height: 63px; background: var(--orange);
    border-radius: 32px 0 0 32px; box-shadow: 0 0 14px rgba(255,122,31,.35);
  }
  .summary-pill .icon {
    left: 4px; top: 4px; width: 55px; height: 55px; border-radius: 50%; background: var(--cream);
    display: flex; align-items: center; justify-content: center;
  }
  .summary-pill .pill-label {
    right: 12px; top: 4px; font-family: "Fredoka", sans-serif; font-weight: 600; font-size: 16px;
    color: var(--panel); text-decoration: underline; text-underline-offset: 2px;
  }
  .summary-pill .pill-value {
    right: 12px; top: 28px; font-family: "Fredoka", sans-serif; font-weight: 700; font-size: 21px;
    color: var(--panel); letter-spacing: .5px;
  }
  .pill-payment { left: 218px; }
  .pill-total { left: 412px; }
  .pill-balance { left: 605px; }

  .wallet-btn {
    left: 796px; top: 606px; width: 185px; height: 63px; border-radius: 32px; background: var(--coral);
    display: flex; align-items: center; justify-content: center;
    font-family: "Fredoka", sans-serif; font-weight: 700; font-size: 21px; color: var(--panel);
    box-shadow: 0 0 14px rgba(255,117,83,.35);
  }

  .scroll-track { left: 404px; top: 720px; width: 392px; height: 8px; background: var(--cream); }
</style>
</head>
<body>

  <header class="abs title-block"></header>
  <h1 class="abs title">INVOICE</h1>
  <div class="abs year-box">2019</div>
  <svg class="abs year-stepper" width="12" height="42" viewBox="0 0 12 42" aria-hidden="true">
    <polygon points="6,0 12,9 0,9" fill="var(--coral)"/>
    <polygon points="0,31 12,31 6,40" fill="var(--coral)"/>
  </svg>

  <div class="abs overview-btn">Year Overview</div>

  <main class="abs panel"></main>

  <svg class="abs donut" width="272" height="272" viewBox="0 0 272 272" role="img" aria-label="Invoice breakdown pie chart">
    <g fill="none" stroke-width="36">
      <circle cx="136" cy="136" r="118" stroke="var(--yellow)" stroke-dasharray="500 742" stroke-dashoffset="-2"/>
      <circle cx="136" cy="136" r="118" stroke="var(--green)" stroke-dasharray="136 742" stroke-dashoffset="-509"/>
      <circle cx="136" cy="136" r="118" stroke="var(--cyan-soft)" stroke-dasharray="86 742" stroke-dashoffset="-651"/>
    </g>
  </svg>
  <div class="abs invoice-id">TKZ19-0037</div>

  <div class="abs style-toggle">
    <div class="abs toggle-pie">PIE</div>
    <div class="abs toggle-bar">BAR</div>
  </div>
  <div class="abs toggle-hint">CLICK TO CHANGE STYLE</div>

  <div class="abs info-card month"><span class="label">MONTH</span><span class="value">Jan 2019</span></div>
  <div class="abs info-card status"><span class="label">STATUS</span><span class="value">Paid</span></div>
  <div class="abs info-card mode"><span class="label">PAYMENT MODE</span><span class="value">Actual</span></div>

  <div class="abs pdf-btn">PDF
    <svg class="abs pdf-edit" width="12" height="12" viewBox="0 0 12 12" aria-hidden="true">
      <path d="M6 2H1v9h9V6" fill="none" stroke="var(--cream)" stroke-width="1.2"/>
      <path d="M4 8l1-3 5-5 2 2-5 5z" fill="none" stroke="var(--cream)" stroke-width="1.1"/>
    </svg>
  </div>

  <div class="abs rule rule-top"></div>

  <div class="abs amount-card received"><span class="label">PAYMENT RECEIVED</span><span class="value">$1243</span></div>
  <div class="abs amount-bar received"></div>
  <div class="abs amount-card extra"><span class="label">EXTRA AFTER CREDIT</span><span class="value">$141</span></div>
  <div class="abs amount-bar extra"></div>
  <div class="abs amount-card contract"><span class="label">CONTRACT PRICE</span><span class="value">$1152</span></div>
  <div class="abs amount-bar contract"></div>

  <div class="abs info-card mini-card open-balance"><span class="label">OPEN BALANCE</span><span class="value">$92</span></div>
  <div class="abs info-card mini-card contract-days"><span class="label">CONTRACT DAYS</span><span class="value">11</span></div>

  <div class="abs rule rule-bottom"></div>

  <div class="abs side-arrow side-prev">
    <svg class="abs" style="left:38px;top:25px" width="16" height="18" viewBox="0 0 16 18" aria-hidden="true"><polygon points="0,9 15,0 15,18" fill="var(--header-bg)"/></svg>
  </div>
  <div class="abs side-arrow side-next">
    <svg class="abs" style="left:15px;top:25px" width="16" height="18" viewBox="0 0 16 18" aria-hidden="true"><polygon points="15,9 0,0 0,18" fill="var(--header-bg)"/></svg>
  </div>

  <div class="abs summary-pill pill-payment">
    <div class="abs icon">
      <svg width="34" height="30" viewBox="0 0 34 30" aria-hidden="true">
        <g fill="none" stroke="var(--header-bg)" stroke-width="2">
          <path d="M2 12h30v16H2z"/><path d="M2 12l15 10 15-10"/>
          <circle cx="17" cy="9" r="7" fill="var(--cream)"/>
        </g>
        <text x="17" y="13" text-anchor="middle" font-family="Montserrat, sans-serif" font-weight="800" font-size="10" fill="var(--header-bg)">$</text>
      </svg>
    </div>
    <div class="abs pill-label">Payment</div>
    <div class="abs pill-value">$10651</div>
  </div>

  <div class="abs summary-pill pill-total">
    <div class="abs icon">
      <svg width="30" height="38" viewBox="0 0 30 38" aria-hidden="true">
        <g fill="none" stroke="var(--header-bg)" stroke-width="2">
          <path d="M2 2h26v34H2z"/>
          <path d="M6 8h18M6 12h18M6 16h18M6 20h10M6 24h10M6 28h10M6 32h10" stroke-width="1.5"/>
        </g>
        <text x="22" y="32" text-anchor="middle" font-family="Montserrat, sans-serif" font-weight="800" font-size="13" fill="var(--header-bg)">$</text>
      </svg>
    </div>
    <div class="abs pill-label">Total Price</div>
    <div class="abs pill-value">$7849</div>
  </div>

  <div class="abs summary-pill pill-balance">
    <div class="abs icon">
      <svg width="38" height="28" viewBox="0 0 38 28" aria-hidden="true">
        <g fill="none" stroke="var(--header-bg)" stroke-width="2">
          <path d="M4 6l30-4v4"/><path d="M2 8h34v18H2z"/>
          <circle cx="26" cy="17" r="4"/><path d="M32 17h3"/>
        </g>
        <text x="11" y="22" text-anchor="middle" font-family="Montserrat, sans-serif" font-weight="800" font-size="13" fill="var(--header-bg)">$</text>
      </svg>
    </div>
    <div class="abs pill-label">Balance</div>
    <div class="abs pill-value">$2802</div>
  </div>

  <div class="abs wallet-btn">MOVE TO WALLET</div>

  <div class="abs scroll-track"></div>

</body>
</html>
```